Step and Repeat Backdrop for wedding reception photo booth

Would like to have a Step and Repeat Backdrop (8 foot high by 10 foot wide) that incorporates the wedding logo (attached) and the names Elena and Gavin. Background should be white, and wedding colors are burgundy and gold. Show me creativity :-) I have included some random samples.

```html
<!DOCTYPE html>
<html lang="en">
<head>
<meta charset="utf-8">
<title>Elena &amp; Gavin — Step and Repeat Backdrop</title>
<link rel="stylesheet" href="https://fonts.googleapis.com/css2?family=Cinzel:wght@400&display=swap">
<style>
  :root {
    --backdrop-white: #ffffff;
    --burgundy: #b0252f;
    --gold: #cdb07a;
    --gold-deep: #b48c45;
  }
  * { margin: 0; padding: 0; box-sizing: border-box; }
  html, body {
    width: 1200px;
    height: 969px;
    overflow: hidden;
    background: var(--backdrop-white);
  }
  .backdrop {
    position: relative;
    width: 1200px;
    height: 969px;
    background: var(--backdrop-white);
    font-family: "Cinzel", "Times New Roman", serif;
    font-weight: 400;
  }
  .name-stack {
    position: absolute;
    width: 240px;
    transform: translate(-50%, -50%);
    text-align: center;
    color: var(--burgundy);
    font-size: 44px;
    line-height: 50px;
    letter-spacing: 0.02em;
  }
  .name-stack .line { display: block; white-space: nowrap; }
  .name-line {
    position: absolute;
    transform: translate(-50%, -50%);
    white-space: nowrap;
    color: var(--gold);
    font-size: 38px;
    letter-spacing: 0.01em;
  }
  .centre-name {
    position: absolute;
    left: 600px;
    top: 479px;
    transform: translate(-50%, -50%);
    white-space: nowrap;
    color: var(--gold-deep);
    font-size: 50px;
  }
</style>
</head>
<body>
<main class="backdrop">
  <div class="name-stack" style="left:198px; top:172px;"><span class="line">Elena</span><span class="line">&amp; Gavin</span></div>
  <div class="name-stack" style="left:600px; top:172px;"><span class="line">Elena</span><span class="line">&amp; Gavin</span></div>
  <div class="name-stack" style="left:1000px; top:172px;"><span class="line">Elena</span><span class="line">&amp; Gavin</span></div>

  <p class="name-line" style="left:387px; top:287px;">Elena &amp; Gavin</p>
  <p class="name-line" style="left:839px; top:287px;">Elena &amp; Gavin</p>

  <div class="name-stack" style="left:198px; top:479px;"><span class="line">Elena</span><span class="line">&amp; Gavin</span></div>
  <p class="centre-name">Elena &amp; Gavin</p>
  <div class="name-stack" style="left:1000px; top:479px;"><span class="line">Elena</span><span class="line">&amp; Gavin</span></div>

  <p class="name-line" style="left:387px; top:674px;">Elena &amp; Gavin</p>
  <p class="name-line" style="left:839px; top:674px;">Elena &amp; Gavin</p>

  <div class="name-stack" style="left:198px; top:803px;"><span class="line">Elena</span><span class="line">&amp; Gavin</span></div>
  <div class="name-stack" style="left:600px; top:803px;"><span class="line">Elena</span><span class="line">&amp; Gavin</span></div>
  <div class="name-stack" style="left:1000px; top:803px;"><span class="line">Elena</span><span class="line">&amp; Gavin</span></div>
</main>
</body>
</html>
```